Meridel Capra SA Business Cards

Dear all,
Thank you for reading my brief and project. My company is doing doing advisory in real estate and to comapnies + real estates services as asset management, brokerage, development etc.
I would like to get a business card for my company which is clear, professionnal and serious.
Please have a look to the attachement to see the logos of the company

Industry/Entity Type

Real Estate

Contact Information for Business Card

I would like to have in the business card the following
Principal side:
- Logo of the company (or Monogram)
- First and Last Name (Paulo Vestrand)
- Mobile number
- email address

Second side:
- Address (Chemin des Orvets 17, 1226 Thônex - Switzerland)
- website (www.meridelcapra.ch)

Requirements
Must have
• Refer to the typeface and logo colors

```html
<!DOCTYPE html>
<html lang="en">
<head>
<meta charset="utf-8">
<title>Meridel Capra SA – Business Card</title>
<link rel="stylesheet" href="https://fonts.googleapis.com/css2?family=Montserrat:wght@600&family=Khand:wght@600&family=Roboto:wght@400&display=swap">
<style>
  :root {
    --page-bg: #e6e4e1;
    --card-bg: #f5f6f7;
    --card-edge: #dcdfe2;
    --brand-blue: #1d6fae;
    --brand-dark: #2e3740;
    --text-grey: #3d4349;
    --icon-blue: #2f5f86;
  }
  * { margin: 0; padding: 0; box-sizing: border-box; }
  html, body {
    width: 1200px;
    height: 1054px;
    overflow: hidden;
    background: var(--page-bg);
  }
  .card {
    position: absolute;
    left: 120px;
    top: 237px;
    width: 960px;
    height: 580px;
    background: var(--card-bg);
    border: 1px solid var(--card-edge);
    box-shadow: 0 6px 24px rgba(0, 0, 0, 0.08);
    overflow: hidden;
  }
  .brand {
    position: absolute;
    left: 125px;
    top: 82px;
    height: 152px;
    display: flex;
    align-items: center;
  }
  .brand-square {
    width: 96px;
    height: 96px;
    background: var(--brand-blue);
  }
  .brand-divider {
    width: 2px;
    height: 152px;
    background: var(--brand-blue);
    margin: 0 34px 0 78px;
  }
  .brand-name {
    font-family: "Montserrat", sans-serif;
    font-weight: 600;
    font-size: 50px;
    letter-spacing: 1px;
    color: var(--brand-dark);
    white-space: nowrap;
  }
  .person {
    position: absolute;
    right: calc(960px - 411px);
    top: 352px;
    text-align: right;
  }
  .person-name {
    font-family: "Khand", sans-serif;
    font-weight: 600;
    font-size: 40px;
    line-height: 1.1;
    color: var(--brand-blue);
  }
  .person-title {
    font-family: "Roboto", sans-serif;
    font-size: 23px;
    color: var(--text-grey);
    margin-top: 4px;
  }
  .section-divider {
    position: absolute;
    left: 464px;
    top: 328px;
    width: 2px;
    height: 150px;
    background: var(--brand-blue);
  }
  .contact {
    position: absolute;
    left: 537px;
    top: 348px;
    list-style: none;
  }
  .contact-item {
    display: flex;
    align-items: center;
    height: 36.5px;
    font-family: "Roboto", sans-serif;
    font-size: 24px;
    color: var(--text-grey);
  }
  .contact-icon {
    width: 22px;
    height: 22px;
    margin-right: 18px;
    fill: var(--icon-blue);
  }
  .card-band {
    position: absolute;
    left: 0;
    bottom: 0;
    width: 100%;
    height: 22px;
    display: flex;
  }
  .card-band-blue { width: 479px; background: var(--brand-blue); }
  .card-band-dark { flex: 1; background: var(--brand-dark); }
</style>
</head>
<body>
  <div class="card">
    <div class="brand">
      <div class="brand-square"></div>
      <div class="brand-divider"></div>
      <div class="brand-name">MERIDEL CAPRA</div>
    </div>

    <div class="person">
      <div class="person-name">Paulo Vestrand</div>
      <div class="person-title">Managing Director</div>
    </div>

    <div class="section-divider"></div>

    <ul class="contact">
      <li class="contact-item">
        <svg class="contact-icon" viewBox="0 0 24 24" aria-hidden="true">
          <path d="M3 9c0-3 4-5 9-5s9 2 9 5l-1 2h-4l-1-2c-1-.4-2-.5-3-.5s-2 .1-3 .5l-1 2H4z"/>
          <path d="M6 12h12l2 8H4zM12 14a2.5 2.5 0 1 0 0 5a2.5 2.5 0 1 0 0-5z"/>
        </svg>
        555-014-2087
      </li>
      <li class="contact-item">
        <svg class="contact-icon" viewBox="0 0 24 24" aria-hidden="true">
          <path d="M2 5h20v14H2zM4 7v1l8 5 8-5V7l-8 5z"/>
        </svg>
        paulo@meridelcapra.ch
      </li>
      <li class="contact-item">
        <svg class="contact-icon" viewBox="0 0 24 24" aria-hidden="true">
          <path d="M12 2a10 10 0 1 0 0 20a10 10 0 1 0 0-20zm0 2c1 0 2.2 2 2.6 5H9.4C9.8 6 11 4 12 4zM4.3 11h3.1c0-.7.1-1.4.2-2H5a8 8 0 0 0-.7 2zm0 2a8 8 0 0 0 .7 2h2.6c-.1-.6-.2-1.3-.2-2zm5.1 2h5.2c.1-.6.2-1.3.2-2H9.2c0 .7.1 1.4.2 2zm-.2-4h5.6c0-.7-.1-1.4-.2-2H9.4c-.1.6-.2 1.3-.2 2zm7.4 0h3.1a8 8 0 0 0-.7-2h-2.6c.1.6.2 1.3.2 2zm0 2c0 .7-.1 1.4-.2 2H19a8 8 0 0 0 .7-2zM12 20c-1 0-2.2-2-2.6-5h5.2C14.2 18 13 20 12 20z"/>
        </svg>
        www.meridelcapra.ch
      </li>
    </ul>

    <div class="card-band">
      <div class="card-band-blue"></div>
      <div class="card-band-dark"></div>
    </div>
  </div>
</body>
</html>
```